Business Card Design Project

Small privately owned salon.

Industry/Entity Type

Business

Contact Information for Business Card

Hair salon.i would like my logo to be my name , Rosalind Marie. Address and phone can go on the front or back. The back will be where I write their appt.
address-527 Willowbend lane York, Pa. 17402
Phone- 717-464-3082

```html
<!DOCTYPE html>
<html lang="en">
<head>
<meta charset="utf-8">
<title>Rosalind Marie – Business Card Presentation</title>
<link rel="stylesheet" href="https://fonts.googleapis.com/css2?family=Pinyon+Script&family=Questrial&family=Roboto+Condensed:wght@300;400;500&display=swap">
<style>
  :root {
    --board: #869a98;
    --white: #ffffff;
    --plum: #4b1d3f;
    --plum-band: #5a2447;
    --red: #e0392f;
    --magenta: #c8104a;
    --teal: #3f8a80;
    --gold: #e8d45a;
    --mustard: #e2c24c;
    --charcoal: #2b2b2b;
    --script-red: #d2232a;
    --ink: #444444;
    --hair-red: #c92f45;
    --hair-yellow: #e3c650;
    --hair-teal: #3f8f86;
  }
  * { box-sizing: border-box; margin: 0; padding: 0; }
  html, body { width: 791px; height: 1200px; overflow: hidden; }
  body { background: var(--board); position: relative; font-family: "Questrial", sans-serif; }

  .slot { position: absolute; overflow: hidden; }
  .card {
    position: absolute; left: 0; top: 0;
    width: 484px; height: 274px;
    transform-origin: top left;
    overflow: hidden;
  }

  /* ---------- front of card ---------- */
  .front { background: var(--bg); }
  .front .artwork {
    position: absolute; inset: 0;
    background: linear-gradient(100deg, var(--bg) 0%, var(--hair-red) 30%, var(--hair-yellow) 52%, var(--hair-teal) 72%, var(--bg) 100%);
    opacity: 0.85;
  }
  .front .name-band {
    position: absolute; left: 0; right: 0; top: 176px; height: 88px;
    background: var(--band);
    color: var(--band-text);
  }
  .front .studio { position: absolute; left: 22px; top: 7px; font-size: 15px; white-space: nowrap; }
  .front .name {
    position: absolute; left: 18px; top: 27px;
    font-size: 54px; letter-spacing: -0.5px; line-height: 1; text-transform: uppercase; white-space: nowrap;
  }
  .front.red   { --bg: var(--red);   --band: var(--plum-band); --band-text: var(--white); }
  .front.plum  { --bg: var(--plum);  --band: var(--mustard);   --band-text: var(--plum); }
  .front.teal  { --bg: var(--teal);  --band: var(--charcoal);  --band-text: var(--white); }
  .front.gold  { --bg: var(--gold);  --band: var(--red);       --band-text: var(--white); }

  /* ---------- appointment back ---------- */
  .back { background: var(--white); }
  .back .header {
    position: absolute; left: 0; right: 0; top: 0; height: 111px;
    background: var(--accent); color: var(--white);
  }
  .back .studio { position: absolute; left: 22px; top: 12px; font-size: 15px; white-space: nowrap; }
  .back .name {
    position: absolute; left: 18px; top: 32px;
    font-size: 54px; letter-spacing: -0.5px; line-height: 1; text-transform: uppercase; white-space: nowrap;
  }
  .back .contact {
    position: absolute; left: 0; right: 0; top: 88px; text-align: center;
    font-family: "Roboto Condensed", sans-serif; font-weight: 300; font-size: 15px; white-space: nowrap;
  }
  .back .sep { margin: 0 6px; }
  .back .prompt {
    position: absolute; left: 0; right: 0; top: 122px; text-align: center;
    font-family: "Pinyon Script", cursive; font-size: 24px; color: var(--script-red);
  }
  .back .days {
    position: absolute; left: 0; right: 0; top: 163px; text-align: center;
    font-family: "Roboto Condensed", sans-serif; font-weight: 300; font-size: 15.5px; color: var(--ink); white-space: nowrap;
  }
  .back .days .sep { color: var(--script-red); margin: 0 3px; }
  .back .fields {
    position: absolute; left: 48px; top: 214px;
    font-family: "Roboto Condensed", sans-serif; font-weight: 300; font-size: 15px; color: var(--ink);
    display: flex; gap: 14px;
  }
  .back .field { display: flex; align-items: flex-end; }
  .back .blank { display: inline-block; border-bottom: 1px solid var(--ink); height: 14px; margin-left: 2px; }
  .back .field.date .blank { width: 172px; }
  .back .field.time .blank { width: 130px; }
  .back .note {
    position: absolute; left: 0; right: 0; top: 242px; text-align: center;
    font-family: "Roboto Condensed", sans-serif; font-weight: 300; font-size: 13px; color: var(--ink);
  }
  .back.plum    { --accent: var(--plum); }
  .back.magenta { --accent: var(--magenta); }
  .back.teal    { --accent: var(--teal); }
  .back.red     { --accent: var(--red); }

  .section-title {
    position: absolute; left: 0; right: 0; top: 636px; text-align: center;
    font-family: "Roboto Condensed", sans-serif; font-weight: 400; font-size: 52px;
    color: var(--white); letter-spacing: -0.5px;
  }
</style>
</head>
<body>

  <!-- Featured pair -->
  <div class="slot" style="left:40px; top:20px; width:412px; height:233px;">
    <div class="card back plum" style="transform:scale(0.85);">
      <div class="header">
        <span class="studio">salon studio</span>
        <span class="name">Rosalind Marie</span>
        <p class="contact">527 Willowbend Lane<span class="sep">II</span>Hartwell, PA 16820<span class="sep">II</span>717-464-3082</p>
      </div>
      <p class="prompt">Your next appointment is on</p>
      <p class="days">Monday<span class="sep">II</span>Tuesday<span class="sep">II</span>Wednesday<span class="sep">II</span>Thursday<span class="sep">II</span>Friday<span class="sep">II</span>Saturday</p>
      <div class="fields"><span class="field date">Date:<span class="blank"></span></span><span class="field time">Time:<span class="blank"></span></span></div>
      <p class="note">Please provide 24 hours notice for cancellations.</p>
    </div>
  </div>

  <div class="slot" style="left:340px; top:245px; width:412px; height:233px;">
    <div class="card front red" style="transform:scale(0.85);">
      <div class="artwork" role="img" aria-label="Illustration of a woman with long flowing multicoloured hair"></div>
      <div class="name-band"><span class="studio">salon studio</span><span class="name">Rosalind Marie</span></div>
    </div>
  </div>

  <h2 class="section-title">ALTERNATE COLOR OPTIONS</h2>

  <!-- Front colour options -->
  <div class="slot" style="left:11px; top:720px; width:245px; height:139px;">
    <div class="card front plum" style="transform:scale(0.506);">
      <div class="artwork" role="img" aria-label="Illustration of a woman with long flowing multicoloured hair"></div>
      <div class="name-band"><span class="studio">salon studio</span><span class="name">Rosalind Marie</span></div>
    </div>
  </div>
  <div class="slot" style="left:273px; top:720px; width:245px; height:139px;">
    <div class="card front teal" style="transform:scale(0.506);">
      <div class="artwork" role="img" aria-label="Illustration of a woman with long flowing multicoloured hair"></div>
      <div class="name-band"><span class="studio">salon studio</span><span class="name">Rosalind Marie</span></div>
    </div>
  </div>
  <div class="slot" style="left:534px; top:720px; width:245px; height:139px;">
    <div class="card front gold" style="transform:scale(0.506);">
      <div class="artwork" role="img" aria-label="Illustration of a woman with long flowing multicoloured hair"></div>
      <div class="name-band"><span class="studio">salon studio</span><span class="name">Rosalind Marie</span></div>
    </div>
  </div>

  <!-- Back colour options -->
  <div class="slot" style="left:14px; top:894px; width:484px; height:274px;">
    <div class="card back magenta">
      <div class="header">
        <span class="studio">salon studio</span>
        <span class="name">Rosalind Marie</span>
        <p class="contact">527 Willowbend Lane<span class="sep">II</span>Hartwell, PA 16820<span class="sep">II</span>717-464-3082</p>
      </div>
      <p class="prompt">Your next appointment is on</p>
      <p class="days">Monday<span class="sep">II</span>Tuesday<span class="sep">II</span>Wednesday<span class="sep">II</span>Thursday<span class="sep">II</span>Friday<span class="sep">II</span>Saturday</p>
      <div class="fields"><span class="field date">Date:<span class="blank"></span></span><span class="field time">Time:<span class="blank"></span></span></div>
      <p class="note">Please provide 24 hours notice for cancellations.</p>
    </div>
  </div>

  <div class="slot" style="left:513px; top:884px; width:260px; height:147px;">
    <div class="card back teal" style="transform:scale(0.537);">
      <div class="header">
        <span class="studio">salon studio</span>
        <span class="name">Rosalind Marie</span>
        <p class="contact">527 Willowbend Lane<span class="sep">II</span>Hartwell, PA 16820<span class="sep">II</span>717-464-3082</p>
      </div>
      <p class="prompt">Your next appointment is on</p>
      <p class="days">Monday<span class="sep">II</span>Tuesday<span class="sep">II</span>Wednesday<span class="sep">II</span>Thursday<span class="sep">II</span>Friday<span class="sep">II</span>Saturday</p>
      <div class="fields"><span class="field date">Date:<span class="blank"></span></span><span class="field time">Time:<span class="blank"></span></span></div>
      <p class="note">Please provide 24 hours notice for cancellations.</p>
    </div>
  </div>

  <div class="slot" style="left:513px; top:1038px; width:260px; height:147px;">
    <div class="card back red" style="transform:scale(0.537);">
      <div class="header">
        <span class="studio">salon studio</span>
        <span class="name">Rosalind Marie</span>
        <p class="contact">527 Willowbend Lane<span class="sep">II</span>Hartwell, PA 16820<span class="sep">II</span>717-464-3082</p>
      </div>
      <p class="prompt">Your next appointment is on</p>
      <p class="days">Monday<span class="sep">II</span>Tuesday<span class="sep">II</span>Wednesday<span class="sep">II</span>Thursday<span class="sep">II</span>Friday<span class="sep">II</span>Saturday</p>
      <div class="fields"><span class="field date">Date:<span class="blank"></span></span><span class="field time">Time:<span class="blank"></span></span></div>
      <p class="note">Please provide 24 hours notice for cancellations.</p>
    </div>
  </div>

</body>
</html>
```